The Tidy Hound - Dog Training Business Card Design

I need a business card design for a new dog training company based in Cronulla NSW called The Tidy Hound. I run puppy pre school classes, adult dog classes and do one on one training in the person's home.
I have studied for 2 years and use positive reinforcement training methods based on how dogs learn. I believe in communicating with our dogs what we want them to do rather than punish them for behaviours we don't like. I would like to see designs that use the colours that are used in my logo (please see attached)
I would like a simple and classic looking design. I don't want cartoon images of dogs or any animal images or drawings on the card. I have created my logo with this mindset. I am open to the subtle use of a dog's tail, paws or paw print.

Target Market(s)

high end area which is why I want a classic looking design
adults aged 25 and over

Industry/Entity Type

Dog Training

Contact Information for Business Card

Marcy Tellwin
ORBIS Trained Professional Dog Trainer
www.thetidyhound-example.com.au
0491837265
marcy@thetidyhound-example.com.au

Font styles to use
Sans Serif

Colors
ffffff
86cae6
757575

Requirements
Must have
• Logo - I am trying to attach my logo and colour palette but it won't allow me. I will contact the company and upload ASAP.
Should not have
• images of dogs or cartoon drawings

```html
<!DOCTYPE html>
<html lang="en">
<head>
<meta charset="utf-8">
<title>The Tidy Hound – Business Card</title>
<link rel="stylesheet" href="https://fonts.googleapis.com/css2?family=Cinzel:wght@600&family=Open+Sans:wght@400;600&display=swap">
<style>
  :root {
    --stage: #e4e1dc;
    --card-white: #f3f3f3;
    --card-blue: #a7c6e0;
    --brand-blue: #7fb1da;
    --ink-grey: #757575;
    --ink-dark: #4a4a4a;
    --white: #ffffff;
  }
  * { margin: 0; padding: 0; box-sizing: border-box; }
  html, body {
    width: 1200px; height: 900px; overflow: hidden;
    background: var(--stage);
  }
  .stage {
    width: 1200px; height: 900px;
    display: flex; flex-direction: column;
    align-items: center; justify-content: center; gap: 48px;
  }
  .card {
    width: 660px; height: 378px;
    position: relative;
    box-shadow: 0 6px 18px rgba(0,0,0,0.14);
  }

  /* Back side */
  .card-back {
    background: var(--card-blue);
    display: flex; align-items: center; justify-content: center; gap: 14px;
  }
  .card-back .brand-name {
    font-family: "Open Sans", sans-serif;
    font-weight: 600; font-size: 34px; letter-spacing: 0.5px;
    color: var(--white);
  }
  .card-back .brand-dot {
    width: 18px; height: 18px; border-radius: 50%;
    background: var(--white);
  }

  /* Front side */
  .card-front {
    background: var(--card-white);
    display: flex; align-items: center;
    padding: 0 50px 0 44px;
  }
  .brand-lockup {
    flex: 0 0 272px;
    display: flex; align-items: center; gap: 10px;
  }
  .brand-lockup .brand-name {
    font-family: "Open Sans", sans-serif;
    font-weight: 600; font-size: 30px; line-height: 1;
    color: var(--ink-grey);
  }
  .brand-lockup .brand-dot {
    width: 16px; height: 16px; border-radius: 50%;
    background: var(--brand-blue);
  }
  .contact-block { padding-left: 34px; }
  .person-name {
    font-family: "Cinzel", serif;
    font-weight: 600; font-size: 21px; letter-spacing: 1px;
    color: var(--ink-dark);
  }
  .person-role {
    margin-top: 6px;
    font-family: "Open Sans", sans-serif;
    font-size: 14px; line-height: 1.45;
    color: var(--brand-blue);
  }
  .contact-list { list-style: none; margin-top: 20px; }
  .contact-item {
    display: flex; align-items: center; gap: 12px;
    font-family: "Open Sans", sans-serif;
    font-size: 15px; line-height: 1.75;
    color: var(--ink-dark);
  }
  .contact-icon { width: 16px; height: 16px; flex: 0 0 16px; }
  .contact-icon * { fill: none; stroke: var(--brand-blue); stroke-width: 1.6; }
  .contact-icon .solid { fill: var(--brand-blue); stroke: none; }
</style>
</head>
<body>
<main class="stage">

  <section class="card card-back" aria-label="Business card, back">
    <span class="brand-name">The Tidy Hound</span>
    <span class="brand-dot"></span>
  </section>

  <section class="card card-front" aria-label="Business card, front">
    <div class="brand-lockup">
      <span class="brand-name">The Tidy Hound</span>
      <span class="brand-dot"></span>
    </div>

    <div class="contact-block">
      <h1 class="person-name">Marcy Tellwin</h1>
      <p class="person-role">ORBIS Trained<br>Professional Dog Trainer</p>

      <ul class="contact-list">
        <li class="contact-item">
          <svg class="contact-icon" viewBox="0 0 16 16" aria-hidden="true">
            <path class="solid" d="M3 2.5l2.4-.5 1.3 3-1.5 1.1a8 8 0 0 0 3.7 3.7l1.1-1.5 3 1.3-.5 2.4c-.2.6-.7.9-1.3.9A11 11 0 0 1 2.1 3.8c0-.6.3-1.1.9-1.3z"/>
          </svg>
          <span>0491837265</span>
        </li>
        <li class="contact-item">
          <svg class="contact-icon" viewBox="0 0 16 16" aria-hidden="true">
            <rect x="1.5" y="3.5" width="13" height="9" rx="1"/>
            <path d="M1.8 4l6.2 5 6.2-5"/>
          </svg>
          <span>marcy@thetidyhound-example.com.au</span>
        </li>
        <li class="contact-item">
          <svg class="contact-icon" viewBox="0 0 16 16" aria-hidden="true">
            <circle cx="8" cy="8" r="6.2"/>
            <ellipse cx="8" cy="8" rx="2.8" ry="6.2"/>
            <path d="M1.8 8h12.4"/>
          </svg>
          <span>www.thetidyhound-example.com.au</span>
        </li>
      </ul>
    </div>
  </section>

</main>
</body>
</html>
```